Landing Page Design for Adult Dating Age Verification (18+)

The objective of this task is to design a visually appealing pre-landing page for the adult dating site "Pivolunda (site: https://pivolunda.example/)" with an age verification mechanism. The pre-landing page will feature two buttons that redirect visitors to the main offer. The design should also include a footer block that includes links to the terms of use, privacy policy, and contact us pages.

Design Requirements:
Develop an age verification section prominently displayed on the pre-landing page.
Design the section to include two buttons labeled "Yes" and "No" for visitors to confirm their age.
Ensure the section is visually appealing and clearly communicates the purpose of age verification.

Visual Appeal:
Create a visually appealing design that aligns with the branding and theme of the "Pivolunda" adult dating site.
Use suitable color schemes, typography, and graphics to enhance the overall visual appeal of the pre-landing page.

Layout and Navigation:
Design an engaging and intuitive layout that encourages visitors to interact with the page and proceed to the main offer.
Ensure clear and visible navigation elements that direct visitors to the main offer or provide additional information.

Responsive Design:
Develop a responsive design that provides a seamless user experience across various devices, including desktop and mobile.
Ensure the design elements and layout adapt well to different screen sizes and resolutions.

File Formats and Assets:
Deliver the final design in PSD, AI, or Sketch format, ensuring that the files are well-organized and layered.
Include any necessary images or assets used in the design, ensuring they are of high quality and optimized for web use.

```html
<!DOCTYPE html>
<html lang="en">
<head>
<meta charset="utf-8">
<title>Pivolunda – Verify Your Age</title>
<link rel="stylesheet" href="https://fonts.googleapis.com/css2?family=Roboto:wght@400;500;700&display=swap">
<style>
  :root {
    --ink: #ffffff;
    --accent: #d9a5d8;
    --pink: #ec1a79;
    --bg-deep: #1d1a24;
    --bg-mid: #3a2f3a;
    --bg-warm: #5a4448;
    --heart: rgba(120, 95, 95, 0.55);
    --line: rgba(255, 255, 255, 0.25);
  }
  * { box-sizing: border-box; margin: 0; padding: 0; }
  html, body { width: 1200px; height: 518px; overflow: hidden; background: var(--bg-deep); }
  body { font-family: "Roboto", sans-serif; color: var(--ink); position: relative; }

  .hero-photo {
    position: absolute; inset: 0;
    background:
      radial-gradient(ellipse 45% 55% at 50% 55%, var(--bg-warm) 0%, transparent 70%),
      radial-gradient(ellipse 30% 40% at 20% 20%, #4a4448 0%, transparent 70%),
      linear-gradient(160deg, var(--bg-mid) 0%, var(--bg-deep) 60%, #2a2230 100%);
  }

  .site-header {
    position: absolute; top: 21px; left: 28px; right: 28px; height: 26px;
    display: flex; justify-content: space-between; align-items: center;
  }
  .brand { display: flex; align-items: center; gap: 8px; font-size: 21px; font-weight: 500; color: var(--accent); }
  .brand-dot { width: 22px; height: 22px; border-radius: 50%; background: var(--accent); }
  .auth-nav { display: flex; gap: 10px; }
  .pill {
    border: 1px solid var(--ink); border-radius: 14px; color: var(--ink);
    font-size: 10px; font-weight: 500; letter-spacing: .3px; line-height: 24px; padding: 0 20px;
    text-decoration: none;
  }

  .headline {
    position: absolute; top: 80px; left: 0; width: 100%; text-align: center;
    font-size: 42px; line-height: 48px; font-weight: 700; letter-spacing: -.5px;
  }
  .headline .domain { color: var(--accent); }
  .tagline {
    position: absolute; top: 127px; left: 0; width: 100%; text-align: center;
    font-size: 18px; line-height: 22px; font-weight: 400;
  }

  .age-check { position: absolute; left: 389px; top: 160px; width: 422px; height: 270px; }
  .age-check .heart-shape { position: absolute; inset: 0; width: 100%; height: 100%; }
  .age-check h2 {
    position: absolute; top: 58px; left: 0; width: 100%; text-align: center;
    font-size: 34px; line-height: 40px; font-weight: 700;
  }
  .age-check p {
    position: absolute; top: 100px; left: 36px; width: 350px; text-align: center;
    font-size: 12.5px; line-height: 16px;
  }
  .choice {
    position: absolute; left: 141px; width: 140px; height: 32px; line-height: 32px;
    border-radius: 16px; text-align: center;
    font-size: 13px; font-weight: 700; color: var(--ink); text-decoration: none;
  }
  .choice-yes { top: 141px; background: var(--pink); }
  .choice-no { top: 173px; border: 1px solid var(--ink); line-height: 30px; top: 174px; }

  .site-footer {
    position: absolute; left: 0; right: 0; top: 472px; height: 46px;
    border-top: 1px solid var(--line);
    display: flex; justify-content: space-between; align-items: center; padding: 0 28px;
    font-size: 9.5px; letter-spacing: .3px;
  }
  .legal-links a { color: var(--ink); text-decoration: none; }
</style>
</head>
<body>
  <div class="hero-photo" role="img" aria-label="Dimly lit photograph of a couple embracing on a bed"></div>

  <header class="site-header">
    <div class="brand"><span class="brand-dot"></span>Pivolunda</div>
    <nav class="auth-nav">
      <a class="pill" href="https://pivolunda.example/">SIGN IN</a>
      <a class="pill" href="https://pivolunda.example/">JOIN NOW</a>
    </nav>
  </header>

  <h1 class="headline">Unlock Love at <span class="domain">Pivolunda.example</span></h1>
  <div class="tagline">Discover Your Perfect Match and Find HER at Pivolunda</div>

  <section class="age-check">
    <svg class="heart-shape" viewBox="0 0 300 280" preserveAspectRatio="none" aria-hidden="true">
      <path d="M150 50 C120 0 0 0 0 90 C0 170 100 220 150 280 C200 220 300 170 300 90 C300 0 180 0 150 50Z" fill="var(--heart)"/>
    </svg>
    <h2>Verify Your Age</h2>
    <p>Nemo enim ipsam voluptatem quia voluptas sit aspernatur sint occaecat cupidatat non</p>
    <a class="choice choice-yes" href="https://pivolunda.example/">Yes</a>
    <a class="choice choice-no" href="https://pivolunda.example/">No</a>
  </section>

  <footer class="site-footer">
    <div class="copyright">COPYRIGHT © 2023 PIVOLUNDA. ALL RIGHTS RESERVED.</div>
    <div class="legal-links">
      <a href="https://pivolunda.example/">TERMS OF USE</a> &nbsp;/&nbsp;
      <a href="https://pivolunda.example/">PRIVACY POLICY</a> &nbsp;/&nbsp;
      <a href="https://pivolunda.example/">CONTACT US</a>
    </div>
  </footer>
</body>
</html>
```